Building company needs a new logo and letterhead design

We need a new and refreshed logo and letterhead design for an existing building company. We specialise in residential as well as commercial building/construction, design and project management. Our company name is Kelbrook Constructions Pty Ltd. Our primary colours that we want to use are black/orange/white. We do renovations/alterations/new homes both residential and commercial. We are a medium sized building company. We want something simple and modern.

Industry/Entity Type

Residential

```html
<!DOCTYPE html>
<html lang="en">
<head>
<meta charset="utf-8">
<title>Kelbrook Constructions – Logo and Letterhead</title>
<link rel="stylesheet" href="https://fonts.googleapis.com/css2?family=Exo+2:wght@600&family=Crimson+Text&display=swap">
<style>
  :root {
    --orange: #f07d00;
    --orange-pale: #fbe2c6;
    --black: #111111;
    --ink: #2a2a2a;
    --grey: #c9c9c9;
    --paper: #ffffff;
    --backdrop: #f3f3f3;
  }
  * { box-sizing: border-box; margin: 0; padding: 0; }
  html, body { width: 1200px; height: 1200px; overflow: hidden; }
  body { background: var(--backdrop); position: relative; font-family: "Crimson Text", Georgia, serif; color: var(--ink); }

  .brand-mark { position: absolute; left: 60px; top: 520px; display: flex; align-items: center; gap: 18px; }
  .brand-square { width: 52px; height: 52px; background: var(--orange); flex: none; }
  .brand-name { font-family: "Exo 2", Arial, sans-serif; font-weight: 600; color: var(--black); line-height: 1.1; }
  .brand-mark .brand-name { font-size: 38px; }
  .brand-mark .brand-name span { display: block; font-size: 22px; }

  .letterhead { position: absolute; left: 500px; top: 160px; width: 640px; height: 900px; background: var(--paper); box-shadow: 0 6px 24px rgba(0,0,0,.18); overflow: hidden; }
  .letterhead-brand { position: absolute; left: 40px; top: 48px; display: flex; align-items: center; gap: 10px; }
  .letterhead-brand .brand-square { width: 30px; height: 30px; }
  .letterhead-brand .brand-name { font-size: 20px; }
  .letterhead-brand .brand-name span { display: block; font-size: 12px; }

  .contact { position: absolute; right: 40px; top: 44px; font-family: "Exo 2", Arial, sans-serif; font-weight: 600; font-size: 12px; line-height: 1.35; color: var(--black); }

  .letter { position: absolute; left: 40px; right: 40px; top: 150px; font-size: 13.5px; line-height: 1.32; }
  .letter p { margin-bottom: 16px; }
  .letter .greeting { margin-bottom: 18px; }
  .letter .gap { margin-top: 36px; }
  .sign-off { margin-top: 30px; }
  .signature { width: 60px; height: 36px; margin: 14px 0 10px; background: linear-gradient(90deg, #d9d9d9, #ededed); border-radius: 4px; }
  .signer { font-size: 12.5px; line-height: 1.35; }

  .corner-square { position: absolute; right: 48px; bottom: 80px; width: 150px; height: 150px; background: var(--orange-pale); }

  .footer-bands { position: absolute; left: 0; bottom: 40px; width: 360px; }
  .footer-bands .band-orange { height: 9px; background: var(--orange); }
  .footer-bands .band-black { height: 9px; background: var(--black); }
  .web { position: absolute; right: 40px; bottom: 34px; font-family: "Exo 2", Arial, sans-serif; font-weight: 600; font-size: 14px; color: var(--black); }
</style>
</head>
<body>

<div class="brand-mark">
  <div class="brand-square"></div>
  <div class="brand-name">KELBROOK<span>Constructions Pty Ltd</span></div>
</div>

<article class="letterhead">
  <div class="letterhead-brand">
    <div class="brand-square"></div>
    <div class="brand-name">KELBROOK<span>Constructions Pty Ltd</span></div>
  </div>

  <address class="contact">
    PO Box 317<br>
    Glenmore NSW 2087<br>
    P 0295550142<br>
    F 0295550187<br>
    M 0400555318<br>
    E m.kelbrook@mailnest.com
  </address>

  <div class="letter">
    <p class="greeting">Hello There,</p>
    <p>Lorem Ipsum is simply dummy text of the printing and typesetting industry. Lorem Ipsum has been the industry's standard dummy text ever since the 1500s, when an unknown printer took a galley of type and scrambled it to make a type specimen book. It has survived not only five centuries, but also the leap into electronic typesetting, remaining essentially unchanged. It was popularised in the 1960s with the release of Lettrix sheets containing Lorem Ipsum passages, and more recently with desktop publishing software like PageComposer including versions of Lorem Ipsum.</p>
    <p>It is a long established fact that a reader will be distracted by the readable content of a page when looking at its layout. The point of using Lorem Ipsum is that it has a more-or-less normal distribution of letters, as opposed to using 'Content here, content here', making it look like readable English. Many desktop publishing packages and web page editors now use Lorem Ipsum as their default model text, and a search for 'lorem ipsum' will uncover many web sites still in their infancy. Various versions have evolved over the years, sometimes by accident, sometimes on purpose (injected humour and the like).</p>
    <p class="gap">Contrary to popular belief, Lorem Ipsum is not simply random text. It has roots in a piece of classical Latin literature from 45 BC, making it over 2000 years old. Richard Hollis, a Latin professor at Ashford College in Vermont, looked up one of the more obscure Latin words, consectetur, from a Lorem Ipsum passage, and going through the cites of the word in classical literature, discovered the undoubtable source. Lorem Ipsum</p>
    <p class="sign-off">Best Regards,</p>
    <div class="signature" role="img" aria-label="Handwritten signature"></div>
    <p class="signer">Northline Studio<br>hello@northlinestudio.com</p>
  </div>

  <div class="corner-square"></div>

  <div class="footer-bands">
    <div class="band-orange"></div>
    <div class="band-black"></div>
  </div>
  <div class="web">www.kelbrookconstructions.com.au</div>
</article>

</body>
</html>
```